Bright Harbor website redesign

We need a redesign for a website: mybrightharbor.com.

I already created a video going over what exactly is needed in the design.

See Video here: https://files.vortexa-share.com/file/d/7kPqLm2Xz9RtYw4Nb8Vc3Hd5Jf6Gs1Aa0/view?usp=sharing

Vortexa Deck shown in Video: https://decks.vortexa-share.com/presentation/d/9QwErTy7UiOpAsDfGhJkLzXcVbNm2Qw3ErTy4UiOpAs/edit?usp=sharing
Updates

Holidays in India so we did not get enough design entries or quality.

Target Market(s)

Dentistry

Industry/Entity Type

Dentistry

Number of Pages Required

1 page

Colors
0094D4
00A9DD
6FCCEA
C7EBF8
E9F6FB
00AB8E
00BBA5
67D7C9
C6EFE9
E9F9F6

Requirements
Must have
• See 13 min video link in description - shows what to do.

```html
<!DOCTYPE html>
<html lang="en">
<head>
<meta charset="utf-8">
<title>Bright Harbor – Creating Healthier Smiles</title>
<link rel="stylesheet" href="https://fonts.googleapis.com/css2?family=Montserrat:wght@600;700;800&family=Mulish:wght@400;600;700&display=swap">
<style>
:root{
  --blue:#0094d4;
  --blue-light:#00a9dd;
  --blue-dark:#0a6f9c;
  --red:#e31e24;
  --green-dark:#1d3a1e;
  --green:#5a9459;
  --green-soft:#6e9f6a;
  --ink:#222;
  --text:#444;
  --muted:#777;
  --bg-soft:#f3f8fb;
  --footer:#232323;
  --footer-bar:#1a1a1a;
  --white:#fff;
  --footer-green:#7cbf5a;
}
*{box-sizing:border-box;margin:0;padding:0}
html,body{width:1200px;height:3992px;overflow:hidden}
body{font-family:"Mulish",sans-serif;color:var(--text);background:var(--white);position:relative}
.section{position:absolute;left:0;width:1200px}
.abs{position:absolute}
.btn{position:absolute;display:flex;align-items:center;justify-content:center;border-radius:20px;color:var(--white);font-family:"Montserrat",sans-serif;font-weight:700;font-size:10px;letter-spacing:.2px;text-transform:uppercase}
.btn-red{background:var(--red)}
.btn-blue{background:var(--blue)}
.heading{font-family:"Montserrat",sans-serif;font-weight:800;text-transform:uppercase;letter-spacing:.3px}
.center{left:0;width:1200px;text-align:center}

/* header */
.site-header{top:0;height:82px;background:var(--white)}
.logo{left:130px;top:22px;font-family:"Mulish",sans-serif;font-weight:700;font-size:22px;color:#6aa84f;display:flex;align-items:center;gap:8px}
.logo i{width:12px;height:12px;border-radius:50%;background:var(--red);display:block}
.top-phone{left:694px;top:15px;font-size:10px;color:var(--ink)}
.top-phone b{color:var(--red);font-weight:700}
.nav{left:390px;top:52px;width:690px;height:20px;font-size:10.5px;color:var(--ink)}
.nav span{position:absolute;top:0;white-space:nowrap}
.nav .active{color:#6aa84f}
.caret{display:inline-block;width:5px;height:5px;border-right:1px solid var(--ink);border-bottom:1px solid var(--ink);transform:rotate(45deg);margin:0 0 2px 4px}

/* hero */
.hero{top:82px;height:451px;background:linear-gradient(90deg,#0e82bd 0%,#0b9ad3 55%,#0aa7da 100%)}
.hero h1{left:130px;top:125px;color:var(--white);font-size:44px;line-height:52px}
.hero p{left:130px;top:238px;color:var(--white);font-size:13px}
.hero-art{left:680px;top:12px;width:430px;height:430px;border-radius:50% 50% 46% 46%;background:radial-gradient(circle at 45% 45%,#f4fbff 0%,#d7eef9 45%,rgba(11,154,211,0) 72%)}

/* team */
.team{top:533px;height:508px;background:radial-gradient(ellipse at 45% 60%,#3f6a3b 0%,#233f22 55%,#142714 100%)}
.team h2{top:68px;color:var(--white);font-size:32px}
.team .name{top:138px;color:var(--white);font-size:23px;font-family:"Mulish",sans-serif}
.team .role{top:168px;color:#dfe9de;font-size:10px}
.arrow{position:absolute;width:10px;height:10px;border-top:2px solid var(--white);border-right:2px solid var(--white)}
.photo{position:absolute;background:linear-gradient(180deg,#e4e8ea,#b9c3c7)}
.photo.dim{background:linear-gradient(180deg,#56764f,#3c5c37)}

/* services */
.services{top:1041px;height:1109px;background:var(--white)}
.services h2{top:67px;font-size:32px;color:var(--ink)}
.svc{position:absolute;width:290px;text-align:center}
.svc .ring{width:76px;height:76px;border:2px solid #1a86b8;border-radius:50%;margin:0 auto;display:flex;align-items:center;justify-content:center}
.svc h3{font-family:"Mulish",sans-serif;font-weight:600;font-size:16.5px;color:var(--ink);margin-top:17px}
.svc p{font-size:10.3px;line-height:15.5px;color:var(--text);margin-top:13px;padding:0 6px}
.svc a{display:inline-block;margin-top:15px;font-size:9.5px;color:var(--red);text-decoration:underline;font-weight:600}

/* reviews */
.reviews{top:2150px;height:511px;background:linear-gradient(180deg,#5d9a5c,#4f8a4f)}
.reviews .kicker{top:68px;color:#e6f0e4;font-size:14px;text-transform:uppercase}
.reviews h2{top:88px;color:var(--white);font-size:31px}
.card{position:absolute;top:155px;width:300px;height:288px;background:var(--white);border-radius:3px}
.avatar{position:absolute;left:13px;top:20px;width:56px;height:56px;border-radius:50%;background:linear-gradient(135deg,#c9b6a6,#6b5a4e)}
.stars{position:absolute;left:80px;top:18px;color:#f6b40e;font-size:13px;letter-spacing:3px}
.card .who{position:absolute;left:80px;top:56px;font-size:16px;color:var(--ink);font-weight:600}
.card .quote{position:absolute;left:23px;top:103px;width:260px;font-size:10.5px;line-height:16.5px;color:var(--text)}
.card .quote em{color:var(--red);font-style:normal}
.card .date{position:absolute;left:23px;top:203px;font-size:10px;color:var(--muted)}
.card .source{position:absolute;left:23px;top:250px;width:260px;font-size:10px;color:var(--text);display:flex;align-items:center}
.card .source .s1{margin-left:auto;color:#3b78d8;font-size:14px}
.card .source .s2{margin-left:16px;color:var(--red);font-weight:700;font-size:13px}
.slide-btn{position:absolute;top:285px;width:30px;height:30px;border:1px solid rgba(255,255,255,.7)}
.slide-btn::after{content:"";position:absolute;top:11px;width:7px;height:7px;border-top:1.5px solid var(--white);border-right:1.5px solid var(--white)}
.slide-btn.prev::after{left:13px;transform:rotate(-135deg)}
.slide-btn.next::after{left:9px;transform:rotate(45deg)}

/* difference */
.difference{top:2661px;height:611px;background:var(--bg-soft)}
.difference .kicker{left:130px;top:78px;font-size:15px;color:var(--ink);text-transform:uppercase}
.difference h2{left:130px;top:98px;font-size:33px;color:var(--ink)}
.difference .copy{left:130px;top:166px;width:535px;font-size:12.6px;line-height:19.5px;color:var(--text)}
.difference .copy p{margin-bottom:12px}
.difference .avail{left:130px;top:519px;font-size:20px;color:var(--ink)}
.difference .avail b{color:var(--red);font-weight:600}
.dif-photo{left:690px;top:75px;width:380px;height:459px;background:linear-gradient(160deg,#8fd3e6 0%,#c9ecf4 45%,#e8c6b0 75%,#b8e3ec 100%)}

/* cta */
.cta{top:3272px;height:306px;background:linear-gradient(90deg,#0b86c2,#0aa0d8)}
.cta .kicker{top:77px;color:#e0f3fb;font-size:14px;text-transform:uppercase}
.cta h2{top:98px;color:var(--white);font-size:32px}
.cta .sub{top:152px;color:var(--white);font-size:19px;font-weight:600}

/* footer */
.footer{top:3578px;height:357px;background:var(--footer)}
.f-title{position:absolute;top:50px;font-family:"Montserrat",sans-serif;font-weight:600;font-size:11.5px;color:var(--footer-green);text-transform:uppercase}
.f-text{position:absolute;font-size:10.5px;line-height:18px;color:#d8d8d8}
.f-ico{display:inline-block;width:12px;vertical-align:-2px;margin-right:6px}
.map{left:450px;top:77px;width:300px;height:162px;background:linear-gradient(135deg,#e8eef0,#d5e3d4 50%,#e4e9ee)}
.social{position:absolute;left:980px;display:flex;align-items:center;font-size:10.5px;color:#d8d8d8}
.social i{width:30px;height:30px;border-radius:50%;background:var(--white);display:block;margin-right:12px}
.bottom-bar{top:3935px;height:57px;background:var(--footer-bar);font-size:10px;color:#cfcfcf;display:flex;align-items:center;justify-content:center}
.bottom-bar b{color:var(--footer-green);font-weight:400;margin:0 4px}
</style>
</head>
<body>

<header class="section site-header">
  <div class="abs logo"><i></i>Bright Harbor</div>
  <div class="abs top-phone">Harborview: <b>(555) 210-4388</b></div>
  <div class="btn btn-blue" style="left:827px;top:5px;width:130px;height:31px">Schedule Online</div>
  <div class="btn btn-red" style="left:961px;top:5px;width:109px;height:31px">Emergency</div>
  <nav class="abs nav">
    <span class="active" style="left:0">Home</span>
    <span style="left:63px">About Us</span>
    <span style="left:140px">Service<i class="caret"></i></span>
    <span style="left:207px">Financing<i class="caret"></i></span>
    <span style="left:288px">Testimonials</span>
    <span style="left:382px">New Patient Visit</span>
    <span style="left:499px">Specials</span>
    <span style="left:571px">Contact Us</span>
    <span style="left:659px">Blog</span>
  </nav>
  <div class="abs" style="left:398px;top:71px;width:18px;height:4px;border-bottom:2px solid var(--red);border-radius:0 0 50% 50%"></div>
</header>

<section class="section hero">
  <h1 class="abs heading">Creating<br>Healthier Smiles</h1>
  <p class="abs">With Advanced Technology and Affordable Treatment</p>
  <div class="btn btn-red" style="left:130px;top:285px;width:154px;height:31px">Book an Appointment</div>
  <div class="abs hero-art" role="img" aria-label="Illustration of a smiling cartoon tooth being brushed"></div>
</section>

<section class="section team">
  <h2 class="abs heading center">Meet Our Team</h2>
  <div class="abs center name">Dr. Ravi Menon</div>
  <div class="abs center role">General Dentist (DDS)</div>
  <span class="arrow" style="left:462px;top:157px;transform:rotate(-135deg)"></span>
  <span class="arrow" style="left:728px;top:157px;transform:rotate(45deg)"></span>
  <div class="photo dim" style="left:302px;top:227px;width:152px;height:207px" role="img" aria-label="Portrait of a team dentist"></div>
  <div class="photo" style="left:524px;top:201px;width:152px;height:233px" role="img" aria-label="Portrait of the featured general dentist"></div>
  <div class="photo dim" style="left:742px;top:227px;width:152px;height:207px" role="img" aria-label="Portrait of a team dentist"></div>
</section>

<section class="section services">
  <h2 class="abs heading center">Our Services</h2>

  <svg width="0" height="0" style="position:absolute">
    <defs>
      <symbol id="tooth" viewBox="0 0 40 40"><path d="M12 6c-5 0-7 5-6 10 1 4 3 6 4 12 1 5 3 7 4 7 2 0 2-4 3-8 1-3 2-3 3 0 1 4 1 8 3 8 1 0 3-2 4-7 1-6 3-8 4-12 1-5-1-10-6-10-3 0-4 2-8 2s-5-2-8-2z" fill="none" stroke="#1a86b8" stroke-width="1.6"/></symbol>
    </defs>
  </svg>

  <div class="svc" style="left:135px;top:135px"><div class="ring"><svg width="42" height="42"><use href="#tooth"/></svg></div><h3>Dental Implants</h3><p>Lost teeth? Live your life better and healthier by having a permanent teeth restoration at My Bright Harbor Dental Office.</p><a>READ MORE</a></div>
  <div class="svc" style="left:455px;top:135px"><div class="ring"><svg width="42" height="42"><use href="#tooth"/></svg></div><h3>Cosmetic Dentistry</h3><p>Dental bridges are an important part of your oral health, created to address a gap in your teeth from having a permanent tooth removed.</p><a>READ MORE</a></div>
  <div class="svc" style="left:775px;top:135px"><div class="ring"><svg width="42" height="42"><use href="#tooth"/></svg></div><h3>Braces</h3><p>Dental bridges are an important part of your oral health, created to address a gap in your teeth from having a permanent tooth removed.</p><a>READ MORE</a></div>

  <div class="svc" style="left:135px;top:369px"><div class="ring"><svg width="42" height="42"><use href="#tooth"/></svg></div><h3>Crowns</h3><p>A dental crown is a tooth-shaped cap that is placed over a damaged or misshapen tooth to improve its structural integrity or appearance.</p><a>READ MORE</a></div>
  <div class="svc" style="left:455px;top:369px"><div class="ring"><svg width="42" height="42"><use href="#tooth"/></svg></div><h3>Bridge</h3><p>Dental bridges are an important part of your oral health, created to address a gap in your teeth from having a permanent tooth removed.</p><a>READ MORE</a></div>
  <div class="svc" style="left:775px;top:369px"><div class="ring"><svg width="42" height="42"><use href="#tooth"/></svg></div><h3>Extractions</h3><p>Tooth extraction is a dental procedure where a tooth is removed from its bone socket. When a tooth is severely damaged</p><a>READ MORE</a></div>

  <div class="svc" style="left:135px;top:603px"><div class="ring"><svg width="42" height="42"><use href="#tooth"/></svg></div><h3>Gum Disease</h3><p>Gum disease, also known as periodontal disease, is an infection of the tissues supporting and around your teeth.</p><a>READ MORE</a></div>
  <div class="svc" style="left:455px;top:603px"><div class="ring"><svg width="42" height="42"><use href="#tooth"/></svg></div><h3>Root Canal</h3><p>You must have heard of the treatment called root canal, but do you know what it is really for? Why this procedure is needed</p><a>READ MORE</a></div>
  <div class="svc" style="left:775px;top:603px"><div class="ring"><svg width="42" height="42"><use href="#tooth"/></svg></div><h3>Dentures</h3><p>If you are out of budget and still want to restore your confident smile, a denture treatment is the right option for you.</p><a>READ MORE</a></div>

  <div class="svc" style="left:135px;top:837px"><div class="ring"><svg width="42" height="42"><use href="#tooth"/></svg></div><h3>Emergency Dentistry</h3><p>If you are out of budget and still want to restore your confident smile, a denture treatment is the right option for you.</p><a>READ MORE</a></div>
  <div class="svc" style="left:455px;top:837px"><div class="ring"><svg width="42" height="42"><use href="#tooth"/></svg></div><h3>Veneers</h3><p>If you are out of budget and still want to restore your confident smile, a denture treatment is the right option for you.</p><a>READ MORE</a></div>
  <div class="svc" style="left:775px;top:837px"><div class="ring"><svg width="42" height="42"><use href="#tooth"/></svg></div><h3>ClearAlign Aligners</h3><p>ClearAlign® are custom, removable clear plastic aligners that can be worn in both the lower and upper jaws to straighten teeth.</p><a>READ MORE</a></div>
</section>

<section class="section reviews">
  <div class="abs center kicker">What Our</div>
  <h2 class="abs heading center">Patients Say About Us</h2>
  <div class="slide-btn prev" style="left:50px"></div>
  <div class="slide-btn next" style="left:1120px"></div>

  <article class="card" style="left:130px">
    <div class="avatar" role="img" aria-label="Reviewer profile photo"></div>
    <div class="stars">★★★★★</div>
    <div class="who">Carla J.</div>
    <div class="quote">I have never been an easy patient. Everything terrifies me. I have had SUCH a great experience with Bright Harbor... Marla in particular has especially been kind and helpful. From the very first time I walked into...<em>More</em></div>
    <div class="date">08 October, 2021</div>
    <div class="source">Source:<span class="s1">Searchly</span><span class="s2">Revvu</span></div>
  </article>
  <article class="card" style="left:450px">
    <div class="avatar" role="img" aria-label="Reviewer profile photo"></div>
    <div class="stars">★★★★★</div>
    <div class="who">Nadia P.</div>
    <div class="quote">I am so happy I found Bright Harbor in Harborview. This is a long over due review since I have been seeing them for almost two years. They are always so friendly, understanding and empathetic when they have to deliver n...<em>More</em></div>
    <div class="date">05 October, 2021</div>
    <div class="source">Source:<span class="s1">Searchly</span><span class="s2">Revvu</span></div>
  </article>
  <article class="card" style="left:770px">
    <div class="avatar" role="img" aria-label="Reviewer profile photo"></div>
    <div class="stars">★★★★★</div>
    <div class="who">Melissa T.</div>
    <div class="quote">Starting coming to this dentist and I wish I could have found them sooner. Everyone here is super nice and helpful. They have everything you need here very clean and modern with upgraded equipment. I've been recommended...<em>More</em></div>
    <div class="date">28 September, 2021</div>
    <div class="source">Source:<span class="s1">Searchly</span><span class="s2">Revvu</span></div>
  </article>
</section>

<section class="section difference">
  <div class="abs kicker">Experience the</div>
  <h2 class="abs heading">Bright Harbor Difference</h2>
  <div class="abs copy">
    <p>Your smile is our #1 priority. At Bright Harbor, we provide affordable and expert dental solutions. Whether you are looking for a family dentist or have any emergency such as needing a root canal in Harborview, we are here for you! We want to keep your teeth healthy inside and out. We don't just clean teeth and send you on your way, we want to get to know you.</p>
    <p>We accept most HMO and PPO insurances. We offer various financing options through CarePay, LendWell and In-House Plans.<br>To constantly strive to achieve the highest level of skills and modern techniques and equipment so we can provide our patients with the best that Dentistry has to offer at our dental office in Harborview, Bay County, CA.</p>
    <p>We provide patients with the best experience you can find in all of Southern California. We provide a comfortable and friendly atmosphere to shatter any fears you may have. We supply you with all the information on your dental health options so you can feel comfortable in the choices you make, whether it's a routine check-up or dental implants in Harborview.</p>
  </div>
  <div class="abs avail">We are available for <b>Emergency and Walk-ins.</b></div>
  <div class="abs dif-photo" role="img" aria-label="Photo of a smiling patient in a dental chair giving a thumbs up"></div>
</section>

<section class="section cta">
  <div class="abs center kicker">Committed to</div>
  <h2 class="abs heading center">Excellence in Oral Health Care</h2>
  <div class="abs center sub">Free Exam and X-Rays for New Patients</div>
  <div class="btn btn-red" style="left:521px;top:210px;width:156px;height:30px">Book an Appointment</div>
</section>

<footer class="section footer">
  <div class="f-title" style="left:130px">Bright Harbor</div>
  <div class="f-text" style="left:130px;top:77px">
    <div><svg class="f-ico" viewBox="0 0 12 12" height="12"><path d="M6 1a3.5 3.5 0 0 0-3.5 3.5C2.5 7 6 11 6 11s3.5-4 3.5-6.5A3.5 3.5 0 0 0 6 1z" fill="var(--footer-green)"/><circle cx="6" cy="4.5" r="1.2" fill="var(--footer)"/></svg>482 Linden Park Ave., Suite B</div>
    <div style="padding-left:18px">Harborview, CA 90410</div>
    <div style="margin-top:15px"><svg class="f-ico" viewBox="0 0 12 12" height="12"><path d="M3 1l2 2.5-1 1.5c.8 1.4 1.6 2.2 3 3l1.5-1L11 9l-1 2C5 11 1 7 1 2z" fill="var(--footer-green)"/></svg>Call Us: (555) 210-4388</div>
    <div style="margin-top:15px"><svg class="f-ico" viewBox="0 0 12 12" height="12"><rect x="1" y="3" width="10" height="7" fill="var(--footer-green)"/><path d="M1 3l5 4 5-4" stroke="var(--footer)" fill="none"/></svg>hello@mybrightharbor.com</div>
    <div style="margin-top:22px">Office Hours:</div>
    <div>Monday 10AM–7PM</div>
    <div>Tuesday 10AM–7PM</div>
    <div>Wednesday 9AM–6PM</div>
    <div>Thursday 9AM–6PM</div>
    <div>Friday 9AM–5PM</div>
    <div>Saturday 9AM–1PM</div>
  </div>

  <div class="f-title" style="left:450px">Map &amp; Directions</div>
  <div class="abs map" role="img" aria-label="Street map showing the Harborview office location"></div>
  <div class="f-text" style="left:450px;top:272px">Other Locations:</div>
  <div class="f-text" style="left:450px;top:290px;width:320px;color:#9aa9b8;line-height:15px">Summit Crest Dental &nbsp;|&nbsp; Lakeview Dental &nbsp;|&nbsp; Bayside Dental &nbsp;|<br>Oakridge Dental &nbsp;|&nbsp; Pier Point Dental</div>

  <div class="f-title" style="left:980px">Review Us</div>
  <div class="social" style="top:76px"><i></i>Circle+</div>
  <div class="social" style="top:123px"><i></i>Revvu</div>
  <div class="social" style="top:170px"><i></i>Friendbook</div>
  <div class="social" style="top:217px"><i></i>Chirper</div>
</footer>

<div class="section bottom-bar">All rights reserved.<b>MyBrightHarbor.com</b>| &nbsp;Disclaimer &amp; Terms &nbsp;| &nbsp;Privacy Policy &nbsp;| &nbsp;Sitemap</div>

</body>
</html>
```